WHERE LANTERNS GATHER

Where Lanterns Gather is the title of my book. The book is written to specifically address a major issue the world over which is the ability of think. Educational system in many parts of the world trains us to DO as supposed to Create. In the new world order, doing will always be inferior to thinking. The book is packed with methodologies and case studies. I need a unique design for the book.
Visual of the human brain as part of the creative element / rendition
Since the book is about creative thinking and innovation, I need a creative masterpiece that will be appealing to the eye on the shelf with a strong connection of curiosity & engagement. I personally am of the opinion that visual of the brain is quite off putting
AUTHOR: TOBENNA ADEKUNLE
PRINTED BY: MERIDIAN LEAF
BOOK SIZE: A5

Target Market(s)

Middle to Senior Level Managers in the Private Sector, Fresh Graduates, Entrepreneurs & SME Owners, Government

Font styles to use
Serif

Colors

Designer to choose colors to be used in the design.

Requirements
Must have
• On the front cover, in addition to the title, it should also have the pay off ''Discover & Discover & Unleash The Power Of Your Creative Mind
• Simple back cover design that allows for authors note etc to be very legible
• another must have is space for authors picture
• Front cover Star Burst (WARNING: this book will be difficult to lend)
Should not have
• Visual of the human brain as part of the creative element / rendition

```html
<!DOCTYPE html>
<html lang="en">
<head>
<meta charset="utf-8">
<title>Where Lanterns Gather — Front Cover</title>
<link rel="stylesheet" href="https://fonts.googleapis.com/css2?family=Cinzel:wght@400;600;700&display=swap">
<style>
  :root {
    --backdrop: #e4e4e6;
    --cover-dark: #160b0a;
    --cover-deep: #2a0e0b;
    --ember: #7a1a0e;
    --flame: #e2780f;
    --flame-light: #f4a623;
    --gold: #d89a22;
    --paper: #f2ece4;
  }
  * { margin: 0; padding: 0; box-sizing: border-box; }
  html, body {
    width: 1200px;
    height: 927px;
    overflow: hidden;
    background: var(--backdrop);
  }
  .canvas {
    position: relative;
    width: 1200px;
    height: 927px;
    display: flex;
    align-items: center;
    justify-content: center;
  }
  .front-cover {
    position: relative;
    width: 594px;
    height: 840px;
    background:
      radial-gradient(ellipse at 50% 40%, var(--cover-deep) 0%, var(--cover-dark) 70%);
    overflow: hidden;
    box-shadow: 0 6px 24px rgba(0,0,0,0.25);
    font-family: "Cinzel", "Times New Roman", serif;
    text-align: center;
  }
  .warning-burst {
    position: absolute;
    top: 34px;
    left: 0;
    right: 0;
    color: var(--paper);
    font-size: 15px;
    letter-spacing: 2px;
    z-index: 2;
  }
  .author-name {
    position: absolute;
    top: 58px;
    left: 0;
    right: 0;
    color: var(--gold);
    font-size: 34px;
    font-weight: 600;
    letter-spacing: 3px;
    z-index: 2;
  }
  .cover-artwork {
    position: absolute;
    top: 120px;
    left: 62px;
    width: 470px;
    height: 500px;
    border-radius: 46% 54% 42% 58% / 52% 44% 56% 48%;
    background:
      radial-gradient(ellipse at 50% 48%, var(--flame-light) 0%, var(--flame) 45%, var(--ember) 78%, transparent 100%);
    filter: blur(1px);
  }
  .title-block {
    position: absolute;
    left: 0;
    right: 0;
    top: 600px;
    z-index: 2;
  }
  .title-lead {
    color: var(--gold);
    font-size: 40px;
    font-weight: 600;
    letter-spacing: 2px;
    line-height: 1;
  }
  .title-main {
    color: var(--gold);
    font-size: 92px;
    font-weight: 600;
    letter-spacing: 4px;
    line-height: 1;
    margin-top: 2px;
  }
  .payoff {
    margin-top: 12px;
    color: var(--paper);
    font-size: 19px;
    letter-spacing: 1.5px;
    line-height: 1.2;
  }
</style>
</head>
<body>
  <main class="canvas">
    <article class="front-cover">
      <p class="warning-burst">WARNING: THIS BOOK WILL BE DIFFICULT TO LEND</p>
      <p class="author-name">TOBENNA ADEKUNLE</p>
      <div class="cover-artwork" role="img" aria-label="Textured orange and red fiery burst with a crouching human silhouette at its centre"></div>
      <header class="title-block">
        <h1>
          <span class="title-lead" style="display:block">WHERE LANTERNS</span>
          <span class="title-main" style="display:block">GATHER</span>
        </h1>
        <p class="payoff">DISCOVER &amp; UNLEASH<br>THE POWER OF YOUR CREATIVE MIND</p>
      </header>
    </article>
  </main>
</body>
</html>
```